Cover of the e-book award-winning national sports figure.

I would like to utilize the picture this attached to this brief. If you could pull the trophies and myself out and place with the new background, that’s what I would like to see . I would like to have a new bookcover design for my e-book. I attached below the original cover and have marked in red. The things that I don’t want on the new cover. I’ve attached a picture that’s not the original. I’m waiting on the high copy. I would like to replace the old logo with the one that I have attached. The website that I would like to have on the book is www.dorianwmaxley.com.
Target Market(s)
Biography
Industry/Entity Type
Sports & motivation?
Requirements
Must have
- Picture of me in the blue suit on the cover the title of the book carving out the path diary of a steady runner
Nice to have
- Utilize the old cover that I have attached for some ideas
Should not have
- The cover should not have anything related to brightvale books Inc.

```html
<!DOCTYPE html>
<html lang="en">
<head>
<meta charset="utf-8">
<title>Carving Out the Path — Cover and Jacket</title>
<link rel="stylesheet" href="https://fonts.googleapis.com/css2?family=Anton&family=Oswald:wght@400;500;700&family=Poppins:ital,wght@0,400;0,500;0,600;1,400;1,500&display=swap">
<style>
  :root {
    --stage: #e4e4e4;
    --blue-top: #2b88d4;
    --blue-mid: #1a5fae;
    --blue-deep: #0b2f66;
    --sky: #7cc0f4;
    --white: #ffffff;
    --band-dark: #222325;
    --band-light: #5a5b5e;
    --ink: #1c1c1c;
    --flap-ink: #2a2a2a;
    --accent-blue: #1c6fd0;
    --photo-suit-a: #3a5f9c;
    --photo-suit-b: #1b3566;
    --photo-action-a: #56708c;
    --photo-action-b: #2a3442;
    --trophy-a: #b9bdc4;
    --trophy-b: #5b4636;
  }
  * { box-sizing: border-box; margin: 0; padding: 0; }
  html, body { width: 1200px; height: 2214px; overflow: hidden; }
  body { background: var(--stage); position: relative; font-family: "Poppins", sans-serif; }

  /* ---------- E-book front cover ---------- */
  .ebook-cover {
    position: absolute; left: 250px; top: 90px; width: 700px; height: 1000px;
    background: linear-gradient(180deg, var(--blue-top) 0%, var(--blue-mid) 45%, var(--blue-deep) 100%);
    overflow: hidden; border-radius: 14px;
    box-shadow: 0 18px 40px rgba(0,0,0,.18);
  }
  .ebook-cover .title-main {
    position: absolute; left: 0; right: 0; top: 28px;
    font-family: "Anton", sans-serif; font-size: 196px; line-height: 1.1;
    color: var(--white); text-align: center; letter-spacing: 1px;
  }
  .title-band {
    position: absolute;
    background: linear-gradient(90deg, var(--band-dark) 0%, var(--band-light) 55%, var(--band-dark) 100%);
  }
  .ebook-cover .title-band { left: 0; right: 0; top: 255px; height: 130px; }
  .ebook-cover .title-band span {
    position: absolute; left: 0; right: 0; top: 8px; text-align: center;
    font-family: "Anton", sans-serif; font-size: 100px; line-height: 1.1; color: var(--white);
  }
  .ebook-cover .subtitle {
    position: absolute; left: 56px; top: 402px;
    font-size: 36px; line-height: 1.1; font-weight: 500; color: var(--white);
  }
  .ebook-cover .subtitle strong { font-weight: 600; }
  .ebook-cover .author {
    position: absolute; left: 56px; top: 520px;
    font-family: "Oswald", sans-serif; font-weight: 700; font-size: 78px; line-height: 1.0;
  }
  .author .first { color: var(--sky); display: block; }
  .author .last { color: var(--white); display: block; }
  .ebook-cover .foreword {
    position: absolute; left: 56px; top: 818px;
    font-family: "Oswald", sans-serif; font-size: 27px; color: var(--white);
    border-bottom: 2px solid var(--white); padding-bottom: 2px;
  }
  .ebook-cover .foreword-name {
    position: absolute; left: 56px; top: 868px;
    font-family: "Poppins", sans-serif; font-size: 40px; line-height: 1.0; color: var(--sky);
  }
  .foreword-name .last { font-weight: 600; display: block; }
  .ebook-cover .photo-author {
    position: absolute; left: 430px; top: 405px; width: 250px; height: 595px;
    border-radius: 110px 110px 0 0;
    background: linear-gradient(180deg, var(--photo-suit-a), var(--photo-suit-b));
  }
  .ebook-cover .photo-trophies {
    position: absolute; left: 262px; top: 700px; width: 180px; height: 300px;
    border-radius: 60px 60px 0 0;
    background: linear-gradient(180deg, var(--trophy-a) 0%, #8a8e95 50%, var(--trophy-b) 100%);
  }

  /* ---------- Dust jacket spread ---------- */
  .jacket {
    position: absolute; left: 50px; top: 1400px; width: 1172px; height: 500px;
    transform: scale(0.9386); transform-origin: top left;
    background: linear-gradient(180deg, #1f74c9 0%, var(--blue-mid) 50%, var(--blue-deep) 100%);
    box-shadow: 0 16px 36px rgba(0,0,0,.2);
    overflow: hidden;
  }
  .flap-panel {
    position: absolute; top: 27px; width: 182px; height: 448px;
    background: var(--white); color: var(--flap-ink);
    font-size: 6.2px; line-height: 1.35; text-align: center; padding: 8px 9px;
  }
  .flap-panel p { margin-bottom: 5px; }
  .flap-back { left: 27px; }
  .flap-front { left: 969px; }
  .flap-note { font-style: italic; font-weight: 500; font-size: 7.5px; margin-bottom: 5px; }
  .flap-front .flap-note { position: absolute; left: 0; right: 0; bottom: 12px; }
  .flap-title {
    font-family: "Oswald", sans-serif; font-weight: 500; font-size: 17px; line-height: 1; color: var(--ink); text-align: left;
  }
  .flap-sub { font-size: 11px; color: var(--accent-blue); text-align: left; margin-bottom: 8px; }
  .flap-bio { display: flex; gap: 4px; text-align: center; }
  .flap-bio .bio-text { flex: 1; }
  .flap-bio .bio-name { color: var(--accent-blue); font-weight: 600; font-size: 8px; }
  .flap-bio .bio-photo {
    width: 56px; height: 168px; border-radius: 24px 24px 4px 4px;
    background: linear-gradient(180deg, #d7c98a, #2c2c2c);
  }
  .flap-visit { font-style: italic; font-weight: 600; font-size: 6.5px; position: absolute; left: 10px; bottom: 8px; }

  .brand-mark {
    display: flex; align-items: center; gap: 5px; justify-content: center;
    font-family: "Poppins", sans-serif; font-weight: 600; color: var(--white);
    font-size: 8px; letter-spacing: .5px;
  }
  .brand-mark .dot { width: 18px; height: 18px; border-radius: 50%; border: 2px solid var(--white); }
  .brand-mark.on-white { color: var(--ink); }
  .brand-mark.on-white .dot { border-color: var(--accent-blue); }
  .flap-back .brand-mark { position: absolute; left: 30px; bottom: 26px; }

  .back-title {
    position: absolute; left: 282px; top: 18px; width: 226px; text-align: center;
    font-family: "Anton", sans-serif; font-size: 72px; line-height: 1.2; color: var(--white);
  }
  .jacket .back-band { left: 287px; top: 112px; width: 216px; height: 43px; }
  .jacket .back-band span {
    display: block; text-align: center; font-family: "Anton", sans-serif; font-size: 30px; line-height: 43px; color: var(--white);
  }
  .back-sub { position: absolute; left: 287px; top: 158px; width: 216px; text-align: center; color: var(--white); font-size: 15px; }
  .back-sub strong { font-weight: 600; }
  .back-photo {
    position: absolute; left: 247px; top: 193px; width: 113px; height: 149px; border: 2px solid var(--white);
    background: linear-gradient(160deg, var(--photo-action-a), var(--photo-action-b));
  }
  .back-intro { position: absolute; left: 375px; top: 195px; width: 152px; color: var(--white); font-size: 6.6px; line-height: 1.4; }
  .back-intro h3 { font-size: 8.5px; font-weight: 500; line-height: 1.2; margin-bottom: 7px; }
  .back-charity { position: absolute; left: 250px; top: 400px; width: 110px; color: var(--white); font-style: italic; font-size: 7.5px; line-height: 1.3; }
  .back-logo { position: absolute; left: 250px; top: 438px; }
  .back-web { position: absolute; left: 250px; top: 474px; color: var(--white); font-style: italic; font-weight: 600; font-size: 7px; }

  .spine { position: absolute; left: 557px; top: 0; width: 56px; height: 500px; }
  .spine-name {
    position: absolute; left: 10px; top: 20px; writing-mode: vertical-rl;
    font-family: "Oswald", sans-serif; font-weight: 700; font-size: 26px; color: var(--white);
  }
  .spine .title-band { left: 0; top: 116px; width: 56px; height: 262px; }
  .spine-title {
    position: absolute; left: 15px; top: 124px; writing-mode: vertical-rl;
    font-family: "Anton", sans-serif; font-size: 18px; color: var(--white); white-space: nowrap;
  }
  .spine-sub {
    position: absolute; left: 18px; top: 384px; writing-mode: vertical-rl;
    font-size: 8px; line-height: 1.1; color: var(--white); white-space: nowrap;
  }
  .spine .brand-mark { position: absolute; left: -8px; top: 460px; width: 72px; flex-direction: column; gap: 2px; font-size: 5.5px; }
  .spine .brand-mark .dot { width: 15px; height: 15px; }

  .front-title {
    position: absolute; left: 640px; top: 16px; width: 312px; text-align: center;
    font-family: "Anton", sans-serif; font-size: 90px; line-height: 1.2; color: var(--white);
  }
  .jacket .front-band { left: 613px; top: 130px; width: 336px; height: 48px; }
  .jacket .front-band span {
    display: block; text-align: center; font-family: "Anton", sans-serif; font-size: 42px; line-height: 48px; color: var(--white);
  }
  .front-sub { position: absolute; left: 646px; top: 195px; color: var(--white); font-size: 17px; line-height: 1.15; font-weight: 500; }
  .front-author { position: absolute; left: 646px; top: 262px; font-family: "Oswald", sans-serif; font-weight: 700; font-size: 34px; line-height: 1.0; }
  .front-foreword { position: absolute; left: 646px; top: 402px; font-family: "Oswald", sans-serif; font-size: 12px; color: var(--white); border-bottom: 1px solid var(--white); }
  .front-foreword-name { position: absolute; left: 646px; top: 428px; font-size: 18px; line-height: 1.0; color: var(--sky); }
  .front-foreword-name .last { font-weight: 600; display: block; }
  .front-photo-author {
    position: absolute; left: 836px; top: 200px; width: 112px; height: 300px; border-radius: 50px 50px 0 0;
    background: linear-gradient(180deg, var(--photo-suit-a), var(--photo-suit-b));
  }
  .front-photo-trophies {
    position: absolute; left: 752px; top: 340px; width: 90px; height: 160px; border-radius: 30px 30px 0 0;
    background: linear-gradient(180deg, var(--trophy-a), #8a8e95 50%, var(--trophy-b));
  }
</style>
</head>
<body>

<section class="ebook-cover" aria-label="E-book front cover">
  <h1 class="title-main">CARVING</h1>
  <div class="title-band"><span>OUT THE PATH</span></div>
  <p class="subtitle">Diary of<br><strong>A Steady Runner</strong></p>
  <div class="photo-trophies" role="img" aria-label="Two silver championship trophies on a small wooden side table"></div>
  <div class="photo-author" role="img" aria-label="The author standing in a blue pinstripe suit"></div>
  <p class="author"><span class="first">DORIAN</span><span class="last">MAXLEY</span></p>
  <p class="foreword">FORWORDED BY</p>
  <p class="foreword-name">MARCUS<span class="last">DELANE</span></p>
</section>

<section class="jacket" aria-label="Print jacket spread">
  <div class="flap-panel flap-back">
    <p class="flap-note">(Continued from front flap)</p>
    <p>walk-on, which meant long hours of study and practice through his first season. By his second year he earned a place on special teams and won the trust of coaches who had shaped many great players before him.</p>
    <p>After seasons of steady effort, Maxley became the starting runner and helped his squad to a string of hard-won victories. He set a conference record in a single game, and the pro draft soon followed, opening a long career marked by grit and patience.</p>
    <p>In <b><i>CARVING OUT THE PATH</i></b>, part memoir and part playbook, Maxley shares a framework for becoming a reliable teammate and a steady leader.</p>
    <div class="flap-bio">
      <div class="bio-text">
        <p class="bio-name">DORIAN MAXLEY</p>
        <p>is a former pro fullback who played nine seasons in the league. He speaks to schools, companies and community groups, and supports youth sports programs. He lives in Colorado with his wife and two sons.</p>
        <p><i><b>Visit www.dorianwmaxley.com</b></i></p>
      </div>
      <div class="bio-photo" role="img" aria-label="The author in a casual shirt holding a trophy"></div>
    </div>
    <div class="brand-mark on-white"><span class="dot"></span>DORIAN MAXLEY</div>
    <p class="flap-visit">Visit: www.dorianwmaxley.com</p>
  </div>

  <h2 class="back-title">CARVING</h2>
  <div class="title-band back-band"><span>OUT THE PATH</span></div>
  <p class="back-sub">Diary of <strong>A Steady Runner</strong></p>
  <div class="back-photo" role="img" aria-label="Action photo of a running back carrying the ball"></div>
  <div class="back-intro">
    <h3>From Dorian Maxley's<br>Introduction</h3>
    <p>Becoming a team player is crucial to your ultimate success. Learning to play within a team lifts your own ability and gives you a deep sense of shared achievement. The lessons in this book can be used by any team, whether a sales force, a youth league or a family.</p>
  </div>
  <p class="back-charity">A portion of the proceeds from the sale of this book will be donated to charity.</p>
  <div class="brand-mark back-logo"><span class="dot"></span>DORIAN MAXLEY</div>
  <p class="back-web">www.dorianwmaxley.com</p>

  <div class="spine">
    <p class="spine-name">MAXLEY</p>
    <div class="title-band"></div>
    <p class="spine-title">CARVING OUT THE PATH</p>
    <p class="spine-sub">Diary of<br>A Steady Runner</p>
    <div class="brand-mark"><span class="dot"></span>DORIAN MAXLEY</div>
  </div>

  <h2 class="front-title">CARVING</h2>
  <div class="title-band front-band"><span>OUT THE PATH</span></div>
  <p class="front-sub">Diary of<br>A Steady Runner</p>
  <div class="front-photo-trophies" role="img" aria-label="Two silver championship trophies on a small wooden side table"></div>
  <div class="front-photo-author" role="img" aria-label="The author standing in a blue pinstripe suit"></div>
  <p class="front-author author"><span class="first">DORIAN</span><span class="last">MAXLEY</span></p>
  <p class="front-foreword">FORWORDED BY</p>
  <p class="front-foreword-name">MARCUS<span class="last">DELANE</span></p>

  <div class="flap-panel flap-front">
    <p class="flap-title">CARVING OUT THE PATH</p>
    <p class="flap-sub">Diary of <b>A Steady Runner</b></p>
    <p>As the starting fullback for the Ridgeline Stallions, Maxley cleared the way for his teammates and earned a name as the consummate team player. In this book he explains what it means to be part of something larger, how to master your talent, and how to turn setbacks into growth.</p>
    <p>Raised on the south side of a big city, Maxley chose football at an early age. He moved to a public school with a proud tradition and played under a coach known for shaping young athletes into dedicated professionals.</p>
    <p>Though his name filled local sports pages week after week, his path to college was not simple. Overlooked by many, he chose to walk on at the state university and earn his place.</p>
    <p class="flap-note">(Continued on back flap)</p>
  </div>
</section>

</body>
</html>
```